Halloway Crest Backers Guild business cards

Create a single-sided business card for the Halloway Crest Backers Guild based on the attached logo.
The additional data fields include Name, Title, Email, Phone, and website.
Please use the following as sample data:
Name: Dean Varrow
Title: Co-Founder / Investor
Email: deanvarrow@mailtern.net
Phone: 555-314-2706
Website: www.hcbackersguild.com

Target Market(s)

Start ups, entrepreneurs, venture capitalists

Industry/Entity Type

Investment

Contact Information for Business Card

Professional business card. Technology company.

Font styles to use
Serif
Sans Serif

Requirements
Must have
• Include the HCBG logo (attached)
• Name
• Title
• Email
• Phone
• Website
Should not have
• Cute, cartoony

```html
<!DOCTYPE html>
<html lang="en">
<head>
<meta charset="utf-8">
<title>Halloway Crest Backers Guild — Business Card</title>
<link rel="stylesheet" href="https://fonts.googleapis.com/css2?family=Lato:wght@300;400;700;900&display=swap">
<style>
  :root {
    --stage: #2b2b2b;
    --card: #f7f7f7;
    --card-edge: #e6e6e6;
    --green: #1a9a4a;
    --ink: #2f2f2f;
    --muted: #8a8a8a;
    --white: #ffffff;
  }
  * { box-sizing: border-box; margin: 0; padding: 0; }
  html, body {
    width: 1200px;
    height: 873px;
    overflow: hidden;
    background: var(--stage);
    font-family: "Lato", sans-serif;
  }
  .card {
    position: absolute;
    left: 180px;
    top: 196px;
    width: 840px;
    height: 480px;
    background: linear-gradient(160deg, var(--white) 0%, var(--card) 55%, var(--card-edge) 100%);
  }
  .brand {
    position: absolute;
    left: 64px;
    top: 96px;
    display: flex;
    align-items: center;
    gap: 22px;
  }
  .brand-mark {
    width: 44px;
    height: 44px;
    background: var(--green);
  }
  .brand-name {
    font-weight: 700;
    font-size: 30px;
    line-height: 1.08;
    color: var(--ink);
    letter-spacing: 0.5px;
  }
  .contact {
    position: absolute;
    left: 480px;
    top: 200px;
    width: 300px;
  }
  .person-name {
    font-weight: 900;
    font-size: 26px;
    color: var(--green);
    padding-bottom: 4px;
    border-bottom: 2px solid var(--green);
  }
  .person-title {
    margin-top: 6px;
    font-weight: 300;
    font-size: 17px;
    color: var(--muted);
  }
  .contact-list {
    list-style: none;
    margin-top: 22px;
  }
  .contact-item {
    display: flex;
    align-items: center;
    gap: 14px;
    font-size: 19px;
    color: var(--ink);
    margin-bottom: 14px;
  }
  .contact-icon {
    width: 26px;
    height: 26px;
    flex: none;
  }
  .website {
    margin-top: 4px;
    font-weight: 900;
    font-size: 18px;
    letter-spacing: 3px;
    color: var(--green);
  }
</style>
</head>
<body>
  <main class="card">
    <div class="brand">
      <div class="brand-mark"></div>
      <div class="brand-name">Halloway Crest<br>Backers Guild</div>
    </div>

    <section class="contact">
      <h1 class="person-name">Dean Varrow</h1>
      <p class="person-title">Co-Founder / Investor</p>
      <ul class="contact-list">
        <li class="contact-item">
          <svg class="contact-icon" viewBox="0 0 26 26" aria-hidden="true">
            <circle cx="13" cy="13" r="13" fill="var(--green)"/>
            <path d="M8 9.5c0-1 1-1.8 2-1.5l1.2 2.2-1 1c.7 1.6 2 2.9 3.6 3.6l1-1 2.2 1.2c.3 1-.5 2-1.5 2C11 17 8 14 8 9.5z" fill="var(--white)"/>
          </svg>
          <span>555-314-2706</span>
        </li>
        <li class="contact-item">
          <svg class="contact-icon" viewBox="0 0 26 26" aria-hidden="true">
            <circle cx="13" cy="13" r="13" fill="var(--green)"/>
            <rect x="7" y="9" width="12" height="8.5" fill="none" stroke="var(--white)" stroke-width="1.5"/>
            <path d="M7 9l6 5 6-5" fill="none" stroke="var(--white)" stroke-width="1.5"/>
          </svg>
          <span>deanvarrow@mailtern.net</span>
        </li>
      </ul>
      <p class="website">www.hcbackersguild.com</p>
    </section>
  </main>
</body>
</html>
```